依頼詳細
<使用してもらいたい文言:パターン①>
・マウスピース矯正クリアフォルテ治療実績2197症例
・北海道No1の症例数(2019,2020,2021年)
<使用してもらいたい文言:パターン②>
・透明で目立たないマウスピース矯正
・頭金0円、月々払いで10800円~
・矯正相談、オンライン相談も受付可能
サイトURL
http://moriwave-orthodontic.example/
ページ数
1ページ
希望イメージ
シンプル 複雑
単色 カラフル
暗い 明るい
日常 高級
遊び心 厳粛
未来的 伝統的
女性的 男性的
希望する色
赤系、黄・オレンジ系、水色系
納品ファイル
• 高解像度JPG (.jpg)
補足説明
デザイン参考サイトは添付しています
PC版だけでなくスマホ版の作成もお願いします。
8〜9割はスマホからのアクセスなので、スマホ版のメインビジュアルを一番重要視しています。
スマホ版のサイズですが、添付画像の赤枠内に入るようなビジュアルでお願いします。

参考にもう一つのメインビジュアルの画像を添付します。

<使用してもらいたい文言:パターン③>
・オンライン診療で6ヶ月に1回の通院からOK
・他院で断られた方もOK
・スピード矯正で3ヶ月で綺麗な前歯に
■ 選んだ理由

当院の強みについての訴求がしっかりとできていた。

■ 提案者全員のお礼・コメント

良い提案をしていただいた方が3名ほどいらっしゃいました。そちらの方を当選と次点とさせていただきました。
今後もこのような機会があると思いますので、みなさま今後ともよろしくお願いいたします。

```html
<!DOCTYPE html>
<html lang="ja">
<head>
<meta charset="utf-8">
<title>もりなみ歯科マウスピース矯正歯科</title>
<link href="https://fonts.googleapis.com/css2?family=Noto+Sans+JP:wght@400;500;700&family=Noto+Serif+JP:wght@500;700;900&display=swap" rel="stylesheet">
<style>
:root{
  --ink:#3a3a3a;
  --white:#ffffff;
  --orange:#f08a1c;
  --orange-light:#f7a94a;
  --orange-deep:#e8731a;
  --blue:#21a3e8;
  --gold:#c9a24a;
  --gold-light:#f1e2b4;
  --bar:#555555;
  --red:#e3401f;
  --brand:#2a6f9e;
}
*{margin:0;padding:0;box-sizing:border-box}
html,body{width:706px;height:1200px;overflow:hidden;background:var(--white)}
body{font-family:"Noto Sans JP",sans-serif;color:var(--ink);position:relative}
.header{position:absolute;left:0;top:0;width:706px;height:94px;background:var(--white);display:flex;align-items:center}
.clinic-name{margin-left:22px;font-size:30px;font-weight:500;letter-spacing:1px;color:var(--ink)}
.header-call,.header-menu{position:absolute;top:0;width:59px;height:94px;display:flex;align-items:center;justify-content:center}
.header-call{left:588px;background:var(--orange-light)}
.header-menu{left:647px;background:var(--blue)}
.hero{position:absolute;left:0;top:94px;width:706px;height:576px;overflow:hidden}
.hero-photo{position:absolute;inset:0;background:linear-gradient(110deg,#f4f4f6 0%,#eeeaea 45%,#e7d3c8 70%,#d9c0b3 100%)}
.hero-copy{position:absolute;top:26px;left:80px;height:410px;writing-mode:vertical-rl;font-family:"Noto Serif JP",serif;font-weight:700;font-size:48px;line-height:70px;color:#4a4a4a;letter-spacing:3px}
.hero-copy span{display:block}
.brand{position:absolute;left:58px;top:496px;display:flex;align-items:center;gap:14px}
.brand-dot{width:40px;height:40px;border-radius:50%;background:var(--brand)}
.brand-name{font-size:36px;font-weight:500;color:var(--brand);letter-spacing:1px}
.consult-band{position:absolute;left:0;top:670px;width:706px;height:54px;background:linear-gradient(90deg,var(--orange-deep),var(--orange-light) 50%,var(--orange-deep));color:var(--white);font-family:"Noto Serif JP",serif;font-weight:700;font-size:32px;display:flex;align-items:center;justify-content:center;letter-spacing:1px}
.speed{position:absolute;left:46px;top:748px;font-family:"Noto Serif JP",serif;font-weight:700;font-size:22px;color:var(--ink);white-space:nowrap}
.speed .accent{color:var(--orange-deep);font-size:36px}
.doctor-photo{position:absolute;left:59px;top:812px;width:318px;height:223px;background:linear-gradient(135deg,#d9dfe6,#a9b4c0 50%,#7a3b4e)}
.badge{position:absolute;left:468px;top:802px;width:214px;height:214px}
.badge-ring{position:absolute;inset:0;border-radius:50%;background:radial-gradient(circle,var(--white) 56%,var(--gold-light) 62%,var(--gold) 72%,var(--white) 74%)}
.badge-text{position:absolute;inset:0;display:flex;align-items:center;justify-content:center;font-family:"Noto Serif JP",serif;font-weight:900;color:var(--gold)}
.badge-label{writing-mode:vertical-rl;font-size:30px;background:var(--gold);color:var(--white);padding:5px 2px;margin-right:6px}
.badge-zero{font-size:104px;line-height:1}
.badge-yen{font-size:36px;align-self:flex-end;margin-bottom:58px}
.monthly{position:absolute;left:440px;top:1022px;font-family:"Noto Serif JP",serif;font-weight:700;font-size:28px;color:var(--gold)}
.action-bar{position:absolute;left:0;top:1070px;width:706px;height:130px;background:var(--bar)}
.call-button{position:absolute;left:12px;top:12px;width:416px;height:106px;background:var(--white);border-radius:8px;display:flex;align-items:center;overflow:hidden}
.call-icon{width:72px;height:106px;background:var(--orange-light);display:flex;align-items:center;justify-content:center}
.call-text{flex:1;text-align:center}
.call-label{font-size:22px;color:var(--ink)}
.call-number{font-size:42px;font-weight:700;color:var(--red);letter-spacing:1px;line-height:1.1}
.web-button{position:absolute;left:442px;top:12px;width:165px;height:106px;background:var(--white);border-radius:8px;display:flex;align-items:center;justify-content:center;font-size:26px;color:var(--ink)}
.top-button{position:absolute;left:628px;top:22px;width:72px;height:96px;background:var(--white);border-radius:6px;display:flex;align-items:center;justify-content:center}
</style>
</head>
<body>
<header class="header">
  <div class="clinic-name">もりなみ歯科マウスピース矯正歯科</div>
  <div class="header-call">
    <svg width="30" height="30" viewBox="0 0 24 24"><path fill="#fff" d="M6.6 10.8c1.4 2.8 3.8 5.1 6.6 6.6l2.2-2.2c.3-.3.7-.4 1-.2 1.1.4 2.3.6 3.6.6.6 0 1 .4 1 1V20c0 .6-.4 1-1 1C10.6 21 3 13.4 3 4c0-.6.4-1 1-1h3.5c.6 0 1 .4 1 1 0 1.3.2 2.5.6 3.6.1.3 0 .7-.2 1z"/></svg>
  </div>
  <div class="header-menu">
    <svg width="30" height="26" viewBox="0 0 30 26"><rect y="2" width="30" height="3" fill="#fff"/><rect y="11.5" width="30" height="3" fill="#fff"/><rect y="21" width="30" height="3" fill="#fff"/></svg>
  </div>
</header>

<section class="hero">
  <div class="hero-photo" role="img" aria-label="透明なマウスピースを手に微笑む女性の写真"></div>
  <h1 class="hero-copy"><span>透明で目立たない</span><span>マウスピース矯正</span></h1>
  <div class="brand"><span class="brand-dot"></span><span class="brand-name">clearforte</span></div>
</section>

<div class="consult-band">矯正相談・オンライン相談も受付可能</div>

<p class="speed">スピード矯正で <span class="accent">3ヶ月</span>で綺麗な前歯に</p>
<div class="doctor-photo" role="img" aria-label="モニターで歯型を説明する医師の写真"></div>

<div class="badge">
  <div class="badge-ring" role="img" aria-label="金色の月桂冠の飾り"></div>
  <div class="badge-text"><span class="badge-label">頭金</span><span class="badge-zero">0</span><span class="badge-yen">円</span></div>
</div>
<p class="monthly">月々10,800円~</p>

<nav class="action-bar">
  <div class="call-button">
    <div class="call-icon">
      <svg width="36" height="36" viewBox="0 0 24 24"><path fill="#fff" d="M6.6 10.8c1.4 2.8 3.8 5.1 6.6 6.6l2.2-2.2c.3-.3.7-.4 1-.2 1.1.4 2.3.6 3.6.6.6 0 1 .4 1 1V20c0 .6-.4 1-1 1C10.6 21 3 13.4 3 4c0-.6.4-1 1-1h3.5c.6 0 1 .4 1 1 0 1.3.2 2.5.6 3.6.1.3 0 .7-.2 1z"/></svg>
    </div>
    <div class="call-text">
      <div class="call-label">電話予約・問合わせ</div>
      <div class="call-number">011-555-0186</div>
    </div>
  </div>
  <div class="web-button">WEB予約</div>
  <div class="top-button">
    <svg width="44" height="52" viewBox="0 0 44 52"><path fill="#555" d="M22 2 42 24H30v26H14V24H2z"/></svg>
  </div>
</nav>
</body>
</html>
```